Halvorsen Spa

We are a large Miami Beach spa and salon. I am still building our website but you can use it as a resource to gain a better understanding of who we are ....www.spaquillowave.com.

We offer a comprehensive list of services in hair, nails, massage, skin care, tanning, spray tanning and waxing and we offer high quality products for skin care, tanning and hair. We are open 7 days.

We would like to see a clean and simple menu that looks a lot like the one from "The Spa at Brightmere." In particular, we have a copy of a menu from their West Hollywood, CA location that is just beautiful. In the uploaded content you will see a sampling of that menu. We would like to see greys, blacks, silvers, whites and warm colors like reds and oranges. We specifically attempt to remain gender neutral so that we don't attract only girls (with pink colors and flowers etc). The final design should convey a simple, clean, friendly environment and the final product should be sized such that it is 1.) portable and 2.) inexpensive to print. We will be running thousands of these at a time so cost of printing is a consideration.

The booklet consists of two parts: one part is the standard menu with descriptions of services and products and photos etc (think of this as the sales piece that convinces a potential customer to visit) and will be stapled together like you would expect a small menu to be and should resemble the Brightmere menu. The prices should not be included in this part of the booklet that will be printed and stapled. The other part is a single insert and is removable and replaceable. I want this removable insert placed in the last page of the book in a folder pocket or something else that you can think of so that when it's time to change prices here that I am not throwing away all of the booklets....I am only replacing the inserts at the end of the menu booklet. Please design this single page insert so that should a customer remove it from the booklet and keep it, that it stands alone with our name, logo, website and phone number. This page can and probably will have to be 2 sided.

At the back of the booklet, I also want the polices to be printed in one page (think fine print in any sort of business dealing.)

With regard to the look and feel slider of economical v upmarket...we definitely want to convey we deliver upmarket services at reasonable prices. Think, world class services and products at reasonable, everyday prices.

With regard to the uploaded files:
I uploaded both EPS and TIF formats. The colors in those files are not the palette we want at all. The colors we want use for the circular logo must match the standard colors as depicted in the uploaded file "Halvorsentanrooms"

Target Market(s)

The target market is the average 20-35 year old in Miami Beach that cares about their appearance. The range of clientele is quite diverse.

Industry/Entity Type

Environment

Requirements
Must have
• It must have elegant and simple photographs that relate to the services being offered. We are selling a service set and an environment...so this menu should be reflect that goal. The logo should be repeated often throughout the book but in subtle ways.

Stock photos are fine as long as they don't seem obviously stock.

Should not have
• Nothing buddha like. Nothing themed. It should be all inclusive and not seek to identify with any particular group or gender.

Nothing that fits the stereotype of "Miami Beach." We want to represent ourselves in the same category as the best spas in the world because we moving everything we do in that direction. Think class!

```html
<!DOCTYPE html>
<html lang="en">
<head>
<meta charset="utf-8">
<title>Halvorsen Spa — Hair Menu</title>
<link rel="stylesheet" href="https://fonts.googleapis.com/css2?family=Jost:wght@300;400&family=Cormorant+Garamond:wght@500&display=swap">
<style>
  :root {
    --panel-dark: #2a2a2a;
    --panel-mid: #4a4a4a;
    --copper: #b35a44;
    --band: rgba(200, 200, 200, 0.32);
    --bar-grey: #9a9a9a;
    --text-light: #e6e6e6;
    --text-soft: #cfcfcf;
    --ghost: rgba(210, 210, 210, 0.42);
    --white: #ffffff;
  }
  * { margin: 0; padding: 0; box-sizing: border-box; }
  html, body {
    width: 1200px; height: 423px; overflow: hidden;
    background: var(--panel-dark);
  }
  .spread {
    position: relative; width: 1200px; height: 423px; overflow: hidden;
    background: radial-gradient(ellipse 60% 70% at 68% 48%, var(--panel-mid), var(--panel-dark) 75%, #1c1c1c);
    font-family: "Jost", "Helvetica Neue", Arial, sans-serif;
  }
  .spread__art { position: absolute; inset: 0; }
  .title-band {
    position: absolute; left: 0; top: 22px; width: 1200px; height: 47px;
    background: var(--band);
    border-top: 1px solid rgba(255,255,255,0.35);
    border-bottom: 1px solid rgba(255,255,255,0.25);
  }
  .ghost-word {
    position: absolute; left: 12px; top: -18px;
    font-weight: 300; font-size: 160px; letter-spacing: 2px;
    color: var(--ghost); line-height: 1;
  }
  .menu-title {
    position: absolute; right: 40px; top: 16px;
    font-weight: 300; font-size: 60px; line-height: 1;
    color: var(--white); letter-spacing: 1px;
  }
  .brand {
    position: absolute; left: 640px; top: 120px; width: 72px;
    text-align: center; color: #a9a9a9;
  }
  .brand__dot {
    display: block; width: 22px; height: 22px; margin: 0 auto 5px;
    border: 1.5px solid #a9a9a9; border-radius: 50%;
  }
  .brand__name {
    font-family: "Cormorant Garamond", Georgia, serif; font-weight: 500;
    font-size: 11px; letter-spacing: 0.5px; white-space: nowrap;
  }
  .service-group { position: absolute; width: 156px; }
  .service-group__head {
    height: 12px; background: var(--bar-grey);
    color: var(--white); font-size: 10.5px; letter-spacing: 1px;
    text-align: center; line-height: 12px; text-transform: uppercase;
    font-weight: 400;
  }
  .service-group__list {
    list-style: none; margin-top: 10px;
    font-size: 8px; line-height: 10px; color: var(--text-soft);
  }
  .group--cutting { left: 768px; top: 121px; }
  .group--extensions { left: 956px; top: 121px; }
  .group--styling { left: 770px; top: 205px; }
  .group--coloring { left: 957px; top: 205px; }
  .group--treatments { left: 770px; top: 302px; }
</style>
</head>
<body>
<main class="spread">
  <svg class="spread__art" width="1200" height="423" viewBox="0 0 1200 423">
    <defs>
      <linearGradient id="portrait-tones" x1="0" y1="0" x2="1" y2="1">
        <stop offset="0" stop-color="#3a1a12"/>
        <stop offset="0.3" stop-color="#8e3520"/>
        <stop offset="0.55" stop-color="#d9a58e"/>
        <stop offset="0.8" stop-color="#7a2c1a"/>
        <stop offset="1" stop-color="#2b120c"/>
      </linearGradient>
    </defs>
    <polygon points="0,0 490,0 580,423 0,423" fill="url(#portrait-tones)"
             role="img" aria-label="Portrait photograph of a woman with glossy auburn hair and a bead necklace"/>
    <polygon points="490,0 560,0 636,423 580,423" fill="var(--copper)"/>
    <circle class="watermark-ring" cx="1124" cy="356" r="74" fill="none" stroke="rgba(150,150,150,0.35)" stroke-width="7"/>
  </svg>

  <div class="title-band">
    <span class="ghost-word">HAIR</span>
    <h1 class="menu-title">HAIR MENU</h1>
  </div>

  <div class="brand">
    <span class="brand__dot"></span>
    <span class="brand__name">Halvorsen Spa</span>
  </div>

  <section class="service-group group--cutting">
    <h2 class="service-group__head">Cutting</h2>
    <ul class="service-group__list">
      <li>men's hair cutfrom</li>
      <li>women's wet cutfrom</li>
      <li>women's cut &amp; blowout</li>
    </ul>
  </section>

  <section class="service-group group--extensions">
    <h2 class="service-group__head">Extensions</h2>
    <ul class="service-group__list">
      <li>hair extensions by lumacrest</li>
      <li>extensions repair</li>
      <li>extensions removal</li>
    </ul>
  </section>

  <section class="service-group group--styling">
    <h2 class="service-group__head">Styling</h2>
    <ul class="service-group__list">
      <li>wet head blowout</li>
      <li>shampoo &amp; blowout</li>
      <li>updos or styling</li>
      <li>wedding hair trials</li>
      <li>wedding day hair</li>
    </ul>
  </section>

  <section class="service-group group--coloring">
    <h2 class="service-group__head">Coloring</h2>
    <ul class="service-group__list">
      <li>single process</li>
      <li>partial highlights/lowlights</li>
      <li>full highlights/lowlights</li>
      <li>double process</li>
    </ul>
  </section>

  <section class="service-group group--treatments">
    <h2 class="service-group__head">Treatments</h2>
    <ul class="service-group__list">
      <li>scalp massage + nourishing treatment</li>
      <li>ultra conditioning reconstructor</li>
      <li>keratin by velora treatment</li>
    </ul>
  </section>
</main>
</body>
</html>
```